Doctors clinic requires stationary designed

We require various types of stationary to be design based on the logo (attached). We require the following:
- Letterhead (A4 Portrait)
- Business Card (must include UV spot on rear)
- With compliments slip (DL Landscape)
- Appointments card (Folded A6)

We are a young clinical practice which boasts a modern and sophisticated approach to medicine so we require something which feels fresh and modern. Please include colours represented in the logo (contrasting teal and grey). We are calling for creative minds to put forth their ideas and we will be actively providing feedback on all designs.

thank you

Clinic

```html
<!DOCTYPE html>
<html lang="en">
<head>
<meta charset="utf-8">
<title>Dr Clara Whitfield – With Compliments Slip</title>
<link rel="stylesheet" href="https://fonts.googleapis.com/css2?family=Source+Sans+3:wght@400;600;700&display=swap">
<style>
  :root {
    --teal: #1f9a8a;
    --teal-soft: #e6f3f1;
    --grey-text: #c2c4c6;
    --ink: #2b2b2b;
    --band: #c6c7c9;
    --paper: #ffffff;
  }
  * { margin: 0; padding: 0; box-sizing: border-box; }
  html, body {
    width: 1200px;
    height: 459px;
    overflow: hidden;
    background: var(--paper);
  }
  .slip {
    position: relative;
    width: 1200px;
    height: 459px;
    background: var(--paper);
    font-family: "Source Sans 3", sans-serif;
  }
  .brand-mark {
    position: absolute;
    left: 32px;
    top: 30px;
    width: 98px;
    height: 98px;
  }
  .letterhead {
    position: absolute;
    left: 161px;
    top: 30px;
  }
  .identity {
    display: flex;
    align-items: center;
    height: 30px;
  }
  .practitioner {
    font-size: 22px;
    font-weight: 700;
    color: var(--teal);
    letter-spacing: -0.3px;
  }
  .divider {
    width: 1px;
    height: 26px;
    background: var(--grey-text);
    margin: 0 8px 0 9px;
  }
  .specialty {
    font-size: 13px;
    font-weight: 600;
    color: var(--teal);
  }
  .address {
    margin-top: 14px;
    font-size: 15px;
    line-height: 19px;
    color: var(--grey-text);
  }
  .contact {
    margin-top: 11px;
    font-size: 13px;
    font-weight: 600;
    color: var(--ink);
  }
  .footer-band {
    position: absolute;
    left: 0;
    bottom: 0;
    width: 100%;
    height: 24px;
    background: var(--band);
  }
</style>
</head>
<body>
  <main class="slip">
    <svg class="brand-mark" viewBox="0 0 98 98" aria-hidden="true">
      <circle cx="49" cy="49" r="46" fill="none" stroke="var(--teal)" stroke-width="4"/>
    </svg>

    <header class="letterhead">
      <div class="identity">
        <span class="practitioner">Dr Clara Whitfield</span>
        <span class="divider"></span>
        <span class="specialty">Obstetrician and Gynaecologist</span>
      </div>
      <address class="address" style="font-style: normal;">
        Harbourview Private Hospital<br>
        Suite 4 Spec. Med. Centre (West) Marlow Ave, Harbourview
      </address>
      <p class="contact">drclarawhitfield.com.au | clara@drclarawhitfield.com.au</p>
    </header>

    <div class="footer-band"></div>
  </main>
</body>
</html>
```